Create a Dynamic, Connecting, Professional looking PowerPoint Design master for our company.

Power point design

Target Market: High worth individuals and corporate group
Industry: Sport and services

Landscape format

Should include various slide such as:
Introduction page (photo background- inclusive logo)
Company presentation (with photos of various projects)
Different slide layouts to place general information with large photo & logo (in different sizes) as well as standard elements, such as text boxes, lines, default shapes, etc
Timeline page
Table pages
Various infographic style pages with editable chart
Our service page – Icons
Location page (world map)
Comparaison pages (3 offers to compare)
Closing page – thank you & contact
Page numbering

Colors:
#6ea6fa
#517ed8
#3758b4
#203390
#060d6c
#2EC193
White / Grey and black

Fonts:
Work sans / Helveticanow / Or other suitable.
Creative use of the logo in the slides. The Timrel icon may be used as a small device or large watermark to enhance branding.

The uploaded photos are indicative of the ones that we would like to use (ie: sail racing) there are here for you to include in the design but would need to be easily replaceable by the final photos we would be using.

If you have any questions or need any aditional material, please send me a message and I will try to respond to it as quickly as possible (bearing in mind that my time zone is UTC +2)

Target Market(s)

High worth individuals and corporate groups

Industry/Entity Type

Sport and services (sailing)

Font styles to use
Other font styles liked:
• Work Sans / Helveticanow

Colors
0054AA
0677BA
7BADD7
CADEEF
E8F1F8
00AB8E
00BBA5
67D7C9
C6EFE9
E9F9F6

Requirements
Must have
• Introduction page (photo background- inclusive logo) Company presentation (with photos of various projects) Different slide layouts to place general information with large photo & logo (in different sizes) as well as standard elements, such as text boxes, lines, default shapes, etc Timeline page Table pages Various infographic style pages with editable chart Our service page – Icons Location page (world map) Comparaison pages (3 offers to compare) Closing page – thank you & contact Page numbering
Nice to have
• Creative use of the logo in the slides. The Timrel icon may be used as a small device or large watermark to enhance branding.

```html
<!DOCTYPE html>
<html lang="en">
<head>
<meta charset="utf-8">
<title>Timrel Presentation Master</title>
<link href="https://fonts.googleapis.com/css2?family=Lato:wght@400;700&display=swap" rel="stylesheet">
<style>
:root{
  --page:#a9a9ab;
  --blue:#1553a8;
  --teal:#1fa58a;
  --teal-mid:#5ec6b4;
  --teal-soft:#c9ebe5;
  --teal-pale:#eef8f6;
  --ink:#1d1d1f;
  --grey:#6b6b6b;
  --white:#ffffff;
  --photo-sea:linear-gradient(135deg,#5c7590,#2b3c52 60%,#1c2a3a);
  --photo-deck:linear-gradient(135deg,#d8d8d8,#8a6b64 55%,#40363a);
  --photo-green:linear-gradient(135deg,#3f5a4a,#6f9a48 50%,#24362c);
  --photo-blue:linear-gradient(160deg,#7d97b6,#1f4f88 50%,#123a6a);
  --plan-soft:linear-gradient(180deg,#f6f7f8,#dfe2e6);
}
*{box-sizing:border-box;margin:0;padding:0}
html,body{width:1040px;height:1200px;overflow:hidden}
body{background:var(--page);font-family:"Lato",Arial,sans-serif;color:var(--ink);position:relative}
.slide{position:absolute;width:306px;height:172px;background:var(--white);overflow:hidden}
.c1{left:48px}.c2{left:368px}.c3{left:688px}
.r1{top:41px}.r2{top:229px}.r3{top:418px}.r4{top:607px}.r5{top:796px}.r6{top:985px}
.abs{position:absolute}
.title{position:absolute;font-size:12px;color:var(--blue);font-weight:400;white-space:nowrap}
.title.caps{text-transform:uppercase}
.body-text{position:absolute;font-size:3.6px;line-height:1.55;color:var(--ink)}
.brand{position:absolute;top:14px;right:10px;display:flex;align-items:center;gap:3px;font-size:9px;font-weight:700;color:var(--ink);letter-spacing:.2px}
.brand::before{content:"";width:7px;height:7px;border-radius:50%;background:currentColor}
.brand.light{color:var(--white)}
.social{position:absolute;right:10px;display:flex;flex-direction:column;gap:4px}
.social span{width:4px;height:4px;border:0.8px solid var(--ink);border-radius:1px}
.social.light span{border-color:var(--white)}
.pagenum{position:absolute;right:10px;bottom:8px;width:14px;height:14px;border-radius:50%;background:var(--white);border:1px solid var(--ink);border-right-color:var(--teal);font-size:8px;color:var(--teal);display:flex;align-items:center;justify-content:center}
.wave{position:absolute;right:-40px;bottom:-40px;width:200px;height:80px;border-radius:50%;background:linear-gradient(90deg,rgba(201,235,229,0),var(--teal-soft));transform:rotate(-12deg)}
.photo{position:absolute}
.card{position:absolute;background:var(--teal);color:var(--white);border-radius:2px;text-align:center}
.soft-card{position:absolute;background:var(--teal-pale);border-radius:3px;display:flex;flex-direction:column}
.ico{width:12px;height:12px;border-radius:50%;background:var(--teal);margin:6px auto 4px;flex:none}
.lbl{font-size:4.5px;line-height:1.3;color:var(--ink)}
.sm{font-size:3.2px;color:var(--grey);line-height:1.4}
table{border-collapse:collapse;font-size:3.6px;text-align:center}
th{background:var(--teal);color:var(--white);font-weight:400;padding:3px 4px}
td{padding:1.5px 4px;background:#dfe9ec}
tr:nth-child(odd) td{background:#cdd9dd}
td.vp{background:var(--teal-mid)!important;color:var(--white)}
.stat{position:absolute;background:var(--teal);color:var(--white);border-radius:2px;font-size:7px;padding:3px 6px;line-height:1.1}
.stat small{display:block;font-size:3.5px}
.tl-year{position:absolute;font-size:7px}
.tl-mark{position:absolute;border-radius:50%;border:2px solid var(--ink)}
.tl-label{position:absolute;text-align:center;font-size:4.2px;line-height:1.3;letter-spacing:.3px}
.tl-label .sm{margin-top:2px}
.loc-item{position:absolute;top:133px;width:34px;text-align:center;font-size:3.4px;line-height:1.3;color:#fff}
.loc-item .sm{font-size:2.8px;color:inherit}
</style>
</head>
<body>

<!-- 1 Welcome -->
<section class="slide c1 r1">
  <div class="wave"></div>
  <div class="abs" style="left:38px;top:48px;width:38px;height:38px;border-radius:50%;background:var(--ink)"></div>
  <div class="abs" style="left:84px;top:52px;font-size:36px;font-weight:700;letter-spacing:-1px">TIMREL</div>
  <div class="abs" style="left:100px;top:116px;font-size:7px;color:var(--blue);letter-spacing:11px">WELCOME</div>
  <div class="social" style="top:138px"><span></span><span></span><span></span></div>
</section>

<!-- 2 Introduction -->
<section class="slide c2 r1" style="background:var(--blue)">
  <div class="photo" role="img" aria-label="Racing yacht heeling in open sea" style="left:0;top:29px;width:172px;height:114px;background:var(--photo-sea);clip-path:polygon(0 0,100% 0,88% 100%,0 100%)"></div>
  <div class="brand light">TIMREL</div>
  <div class="title" style="left:180px;top:55px;color:var(--white)">Introduction</div>
  <div class="body-text" style="left:180px;top:80px;width:92px;color:#dce6f5">A wonderful serenity has taken possession of my entire soul, like these sweet mornings of spring which I enjoy with my whole heart. I am alone, and feel the charm of existence in this spot, which was created for the bliss of souls like mine.</div>
  <div class="social light" style="top:140px"><span></span><span></span><span></span></div>
  <div class="pagenum" style="left:16px;right:auto;bottom:10px">2</div>
</section>

<!-- 3 Welcome Message -->
<section class="slide c3 r1">
  <div class="photo" role="img" aria-label="Fleet of racing sailboats at a start line" style="left:126px;top:0;width:180px;height:172px;background:var(--photo-blue);clip-path:ellipse(100% 140% at 100% 60%);border-left:3px solid var(--teal)"></div>
  <div class="brand light">TIMREL</div>
  <div class="body-text" style="left:21px;top:66px;width:92px">A wonderful serenity has taken possession of my entire soul, like these sweet mornings of spring which I enjoy with my whole heart. I am alone, and feel the charm of existence in this spot, which was created for the bliss of souls like mine.</div>
  <div class="title" style="left:171px;top:86px;color:var(--white)">Welcome Message</div>
  <div class="social light" style="top:70px"><span></span><span></span><span></span></div>
  <div class="pagenum">3</div>
</section>

<!-- 4 About Us -->
<section class="slide c1 r2">
  <div class="abs" style="left:0;top:0;width:100%;height:44px;background:var(--blue);clip-path:polygon(0 0,32% 0,30% 100%,0 100%)"></div>
  <div class="abs" style="left:0;bottom:0;width:140px;height:16px;background:var(--blue)"></div>
  <div class="wave"></div>
  <div class="photo" role="img" aria-label="Crew working winches on deck" style="left:0;top:44px;width:170px;height:110px;background:var(--photo-deck);clip-path:polygon(0 0,100% 0,90% 100%,0 100%)"></div>
  <div class="brand">TIMREL</div>
  <div class="title" style="left:181px;top:49px">About Us</div>
  <div class="body-text" style="left:181px;top:71px;width:92px">A wonderful serenity has taken possession of my entire soul, like these sweet mornings of spring which I enjoy with my whole heart. I am alone, and feel the charm of existence in this spot, which was created for the bliss of souls like mine.</div>
  <div class="social" style="top:73px"><span></span><span></span><span></span></div>
  <div class="pagenum">4</div>
</section>

<!-- 5 Meet Our Team -->
<section class="slide c2 r2" style="background:var(--teal-soft)">
  <div class="brand">TIMREL</div>
  <div class="title" style="left:24px;top:22px">Meet Our Team</div>
  <div class="card" style="left:25px;top:49px;width:66px;height:89px"><div style="font-size:5px;margin-top:13px">Manager</div><div class="sm" style="color:#e7f6f3;margin:6px 6px 0">A wonderful serenity has taken possession of my entire soul, like these sweet mornings of spring</div><div class="abs" style="left:11px;bottom:14px;font-size:3.5px">Dana. R</div><div class="abs" role="img" aria-label="Team member portrait" style="right:6px;bottom:5px;width:26px;height:26px;border-radius:50%;background:var(--white)"></div></div>
  <div class="card" style="left:113px;top:49px;width:66px;height:89px"><div style="font-size:5px;margin-top:13px">Manager</div><div class="sm" style="color:#e7f6f3;margin:6px 6px 0">A wonderful serenity has taken possession of my entire soul, like these sweet mornings of spring</div><div class="abs" style="left:11px;bottom:14px;font-size:3.5px">Leon. T</div><div class="abs" role="img" aria-label="Team member portrait" style="right:6px;bottom:5px;width:26px;height:26px;border-radius:50%;background:var(--white)"></div></div>
  <div class="card" style="left:201px;top:49px;width:66px;height:89px"><div style="font-size:5px;margin-top:13px">Manager</div><div class="sm" style="color:#e7f6f3;margin:6px 6px 0">A wonderful serenity has taken possession of my entire soul, like these sweet mornings of spring</div><div class="abs" style="left:11px;bottom:14px;font-size:3.5px">Mira. K</div><div class="abs" role="img" aria-label="Team member portrait" style="right:6px;bottom:5px;width:26px;height:26px;border-radius:50%;background:var(--white)"></div></div>
  <div class="social" style="top:70px"><span></span><span></span><span></span></div>
  <div class="pagenum">5</div>
</section>

<!-- 6 Services -->
<section class="slide c3 r2">
  <div class="wave"></div>
  <div class="brand">TIMREL</div>
  <div class="title" style="left:22px;top:21px">Our Awesome Services</div>
  <div class="soft-card" style="left:22px;top:44px;width:81px;height:60px;padding:7px 11px"><div style="width:8px;height:10px;background:var(--teal);border-radius:1px"></div><div class="lbl" style="margin-top:12px">Description</div><div class="sm" style="margin-top:3px">Get out on the water<br>with a great rate</div></div>
  <div class="soft-card" style="left:112px;top:44px;width:81px;height:60px;padding:7px 11px"><div style="width:12px;height:10px;background:var(--teal);border-radius:1px"></div><div class="lbl" style="margin-top:12px">Description</div><div class="sm" style="margin-top:3px">Get out on the water<br>with a great rate</div></div>
  <div class="soft-card" style="left:200px;top:44px;width:81px;height:60px;padding:7px 11px"><div style="width:11px;height:10px;background:var(--teal);border-radius:1px"></div><div class="lbl" style="margin-top:12px">Description</div><div class="sm" style="margin-top:3px">Get out on the water<br>with a great rate</div></div>
  <div class="abs" style="left:22px;top:116px;width:243px;height:45px;background:var(--teal-mid);border-radius:2px">
    <div class="abs" style="left:13px;top:13px;width:19px;height:19px;border-radius:50%;border:2.5px solid var(--white);border-left-color:#9fdcd1;font-size:3.5px;color:var(--white);display:flex;align-items:center;justify-content:center">68%</div>
    <div class="abs" style="left:40px;top:15px;font-size:7px;color:var(--white)">$ 664.000<div style="font-size:3.5px">Description</div></div>
    <div class="abs" style="left:107px;top:9px;width:135px;color:var(--white)"><div style="font-size:4px">Utilise our financial acuity to yield profits</div><div style="font-size:2.8px;line-height:1.3;margin-top:2px">A wonderful serenity has taken possession of my entire soul, like these sweet mornings of spring which I enjoy with my whole heart. I am alone, and feel the charm of existence in this spot, which was created for the bliss of souls like mine.</div></div>
  </div>
  <div class="social" style="top:73px"><span></span><span></span><span></span></div>
  <div class="pagenum">6</div>
</section>

<!-- 7 Sail Plan -->
<section class="slide c1 r3">
  <div class="abs" style="right:0;top:0;width:150px;height:172px;background:var(--blue);clip-path:ellipse(100% 110% at 100% 100%);border-left:4px solid var(--teal-mid)"></div>
  <div class="brand light">TIMREL</div>
  <div class="title" style="left:22px;top:20px">Tango Sail Plan</div>
  <div class="photo" role="img" aria-label="Technical side profile drawing of the yacht" style="left:20px;top:40px;width:176px;height:72px;background:var(--plan-soft);border-radius:2px"></div>
  <div class="photo" role="img" aria-label="Technical deck plan drawing of the yacht" style="left:20px;top:118px;width:176px;height:34px;background:var(--plan-soft);border-radius:2px"></div>
  <div class="social light" style="top:73px"><span></span><span></span><span></span></div>
  <div class="pagenum">7</div>
</section>

<!-- 8 Interior Plan -->
<section class="slide c2 r3">
  <div class="abs" style="right:0;top:0;width:150px;height:172px;background:var(--blue);clip-path:ellipse(100% 110% at 100% 100%);border-left:4px solid var(--teal-mid)"></div>
  <div class="brand light">TIMREL</div>
  <div class="title" style="left:22px;top:19px">Tango Sail Interior Plan</div>
  <div class="photo" role="img" aria-label="Line drawing of the yacht profile" style="left:22px;top:38px;width:176px;height:72px;background:var(--plan-soft);border-radius:2px"></div>
  <div class="photo" role="img" aria-label="Line drawing of the yacht interior layout" style="left:22px;top:116px;width:176px;height:36px;background:var(--plan-soft);border-radius:2px"></div>
  <div class="social light" style="top:73px"><span></span><span></span><span></span></div>
  <div class="pagenum">8</div>
</section>

<!-- 9 Location -->
<section class="slide c3 r3" style="background:var(--blue)">
  <div class="abs" style="left:0;top:0;width:130px;height:172px;background:var(--teal-mid);clip-path:polygon(0 0,100% 0,120% 100%,0 100%)"></div>
  <div class="brand light">TIMREL</div>
  <div class="title" style="left:24px;top:22px">Location</div>
  <div class="photo" role="img" aria-label="Dotted world map" style="left:48px;top:38px;width:205px;height:82px;background:radial-gradient(ellipse at 40% 50%,rgba(255,255,255,.55),rgba(255,255,255,.15) 70%,transparent 72%)"></div>
  <svg class="abs" style="left:0;top:0" width="306" height="172" viewBox="0 0 306 172">
    <path d="M67 46a6 6 0 0 1 12 0c0 5-6 11-6 11s-6-6-6-11z" fill="#1553a8"/>
    <path d="M114 80a5 5 0 0 1 10 0c0 4-5 9-5 9s-5-5-5-9z" fill="#6ea6fa"/>
    <path d="M148 60a5 5 0 0 1 10 0c0 4-5 9-5 9s-5-5-5-9z" fill="#1fa58a"/>
    <path d="M205 35a6 6 0 0 1 12 0c0 5-6 11-6 11s-6-6-6-11z" fill="#fff"/>
    <path d="M230 88a5 5 0 0 1 10 0c0 4-5 9-5 9s-5-5-5-9z" fill="#fff"/>
    <line x1="54" y1="127" x2="219" y2="127" stroke="#fff" stroke-width=".8"/>
    <g fill="#fff"><circle cx="54" cy="127" r="2.2" fill="#1553a8"/><circle cx="96" cy="127" r="2.2"/><circle cx="137" cy="127" r="2.2"/><circle cx="178" cy="127" r="2.2"/><circle cx="219" cy="127" r="2.2"/></g>
  </svg>
  <div class="loc-item" style="left:37px;color:#0b2a55">Description<div class="sm">Get out on the water</div></div>
  <div class="loc-item" style="left:79px">Description<div class="sm">Get out on the water</div></div>
  <div class="loc-item" style="left:120px">Description<div class="sm">Get out on the water</div></div>
  <div class="loc-item" style="left:161px">Description<div class="sm">Get out on the water</div></div>
  <div class="loc-item" style="left:202px">Description<div class="sm">Get out on the water</div></div>
  <div class="social light" style="top:71px"><span></span><span></span><span></span></div>
  <div class="pagenum">9</div>
</section>

<!-- 10 Table -->
<section class="slide c1 r4">
  <div class="wave"></div>
  <div class="brand">TIMREL</div>
  <div class="title" style="left:22px;top:20px">Partner, Our Main Priority</div>
  <table class="abs" style="left:24px;top:45px;width:258px">
    <tr><th>Prospective Partner</th><th>Product or Service</th><th>Customer Acquisition</th><th>Referral</th><th>Value Proposition</th></tr>
    <tr><td>Partner 01</td><td>Insurance</td><td>$200</td><td>$50</td><td class="vp">$133</td></tr>
    <tr><td>Partner 02</td><td>Phone</td><td>$250</td><td>$80</td><td class="vp">$209</td></tr>
    <tr><td>Partner 03</td><td>Internet</td><td>$125</td><td>$45</td><td class="vp">$244</td></tr>
    <tr><td>Partner 04</td><td>Hotel</td><td>$245</td><td>$139</td><td class="vp">$72</td></tr>
    <tr><td>Partner 05</td><td>Credit Card</td><td>$380</td><td>$140</td><td class="vp">$376</td></tr>
    <tr><td>Partner 06</td><td>Bank</td><td>$400</td><td>$156</td><td class="vp">$125</td></tr>
    <tr><td>Partner 07</td><td>Food</td><td>$550</td><td>$55</td><td class="vp">$225</td></tr>
  </table>
  <div class="body-text" style="left:24px;top:137px;width:205px">A wonderful serenity has taken possession of my entire soul, like these sweet mornings of spring which I enjoy with my whole heart. I am alone, and feel the charm of existence in this spot, which was created for the bliss of souls like mine.</div>
  <div class="social" style="top:74px"><span></span><span></span><span></span></div>
  <div class="pagenum">10</div>
</section>

<!-- 11 Growth chart -->
<section class="slide c2 r4">
  <div class="wave"></div>
  <div class="brand">TIMREL</div>
  <div class="title" style="left:22px;top:22px">Year by Year Growth</div>
  <svg class="abs" style="left:22px;top:52px" width="134" height="108" viewBox="0 0 134 108">
    <rect width="134" height="108" fill="#f4f7f8"/>
    <g stroke="#d5dadc" stroke-width=".4"><line x1="12" y1="10" x2="130" y2="10"/><line x1="12" y1="19" x2="130" y2="19"/><line x1="12" y1="28" x2="130" y2="28"/><line x1="12" y1="37" x2="130" y2="37"/><line x1="12" y1="46" x2="130" y2="46"/><line x1="12" y1="55" x2="130" y2="55"/><line x1="12" y1="64" x2="130" y2="64"/><line x1="12" y1="73" x2="130" y2="73"/><line x1="12" y1="82" x2="130" y2="82"/><line x1="12" y1="91" x2="130" y2="91"/><line x1="12" y1="100" x2="130" y2="100"/></g>
    <g font-size="3" fill="#555" font-family="Lato,sans-serif"><text x="2" y="11">50</text><text x="2" y="29">40</text><text x="2" y="47">30</text><text x="2" y="65">20</text><text x="2" y="83">10</text><text x="4" y="101">0</text><text x="30" y="106">2</text><text x="52" y="106">4</text><text x="74" y="106">6</text><text x="96" y="106">8</text><text x="117" y="106">10</text></g>
    <path d="M22 85 L38 66 L52 70 L66 52 L78 48 L88 76 L98 34 L104 22 L120 24" fill="none" stroke="#1fa58a" stroke-width="1"/>
    <path d="M22 92 L34 86 L46 74 L60 60 L72 46 L84 58 L96 70 L110 58" fill="none" stroke="#5ec6b4" stroke-width="1"/>
    <rect x="52" y="4" width="36" height="16" rx="1" fill="#1fa58a"/>
    <text x="70" y="9" font-size="3" fill="#fff" text-anchor="middle" font-family="Lato,sans-serif">Highest Number</text>
    <text x="70" y="17" font-size="6.5" fill="#fff" text-anchor="middle" font-family="Lato,sans-serif">45,5%</text>
  </svg>
  <div class="abs" style="left:168px;top:51px;font-size:9px;color:var(--ink)">Description</div>
  <div class="body-text" style="left:168px;top:68px;width:112px;font-size:3px">A wonderful serenity has taken possession of my entire soul, like these sweet mornings of spring which I enjoy with my whole heart. I am alone, and feel the charm of existence.</div>
  <div class="stat" style="left:168px;top:91px;width:51px">3,664.000<small>Description</small></div>
  <div class="stat" style="left:234px;top:91px;width:51px">3,664.000<small>Description</small></div>
  <div class="social" style="top:74px"><span></span><span></span><span></span></div>
  <div class="pagenum">11</div>
</section>

<!-- 12 Value to user -->
<section class="slide c3 r4">
  <div class="wave"></div>
  <div class="brand">TIMREL</div>
  <div class="title" style="left:22px;top:21px">Value to user</div>
  <div class="soft-card" style="left:20px;top:44px;width:62px;height:76px;text-align:center"><div class="ico" style="width:19px;height:19px;margin-top:9px"></div><div class="lbl" style="margin-top:8px">Description</div><div class="sm" style="margin-top:2px">Get out on the water<br>with a great rate</div></div>
  <div class="soft-card" style="left:90px;top:44px;width:62px;height:76px;text-align:center"><div class="ico" style="width:19px;height:19px;margin-top:9px"></div><div class="lbl" style="margin-top:8px">Description</div><div class="sm" style="margin-top:2px">Get out on the water<br>with a great rate</div></div>
  <div class="soft-card" style="left:158px;top:44px;width:62px;height:76px;text-align:center;background:var(--teal)"><div class="ico" style="width:19px;height:19px;margin-top:9px;background:var(--white)"></div><div class="lbl" style="margin-top:8px;color:var(--white)">Description</div><div class="sm" style="margin-top:2px;color:#e7f6f3">Get out on the water<br>with a great rate</div></div>
  <div class="soft-card" style="left:227px;top:44px;width:62px;height:76px;text-align:center"><div class="ico" style="width:19px;height:19px;margin-top:9px"></div><div class="lbl" style="margin-top:8px">Description</div><div class="sm" style="margin-top:2px">Get out on the water<br>with a great rate</div></div>
  <div class="abs" style="left:20px;top:129px;width:81px;height:31px;background:var(--teal);border-radius:2px">
    <div class="abs" style="left:5px;top:7px;width:17px;height:17px;border-radius:50%;border:2px solid #9fdcd1;border-right-color:var(--white);font-size:3.3px;color:var(--white);display:flex;align-items:center;justify-content:center">68%</div>
    <div class="abs" style="left:33px;top:9px;font-size:6.5px;color:var(--white)">$ 664.000<div style="font-size:3.3px">Description</div></div>
  </div>
  <div class="body-text" style="left:110px;top:134px;width:152px;font-size:3px;line-height:1.35">A wonderful serenity has taken possession of my entire soul, like these sweet mornings of spring which I enjoy with my whole heart. I am alone, and feel the charm of existence in this spot, which was created for the bliss of souls like mine. I am so happy, my dear friend, so absorbed.</div>
  <div class="social" style="top:74px"><span></span><span></span><span></span></div>
  <div class="pagenum">12</div>
</section>

<!-- 13 Timeline -->
<section class="slide c1 r5">
  <div class="wave"></div>
  <div class="brand">TIMREL</div>
  <div class="title" style="left:21px;top:20px">Timeline</div>
  <div class="tl-year" style="left:19px;top:82px">2020</div>
  <div class="tl-mark" style="left:14px;top:93px;width:31px;height:31px"></div>
  <div class="tl-year" style="left:71px;top:68px">2021</div>
  <div class="tl-mark" style="left:61px;top:80px;width:38px;height:38px;border-width:2.4px"></div>
  <div class="tl-year" style="left:137px;top:50px">2022</div>
  <div class="tl-mark" style="left:118px;top:64px;width:58px;height:58px;border-width:3px"></div>
  <div class="tl-year" style="left:227px;top:29px">2023</div>
  <div class="tl-mark" style="left:197px;top:42px;width:80px;height:80px;border-width:4px"></div>
  <div class="tl-label" style="left:8px;top:130px;width:44px">Timeline 01<div class="sm">Get out on the water with a great rate</div></div>
  <div class="tl-label" style="left:58px;top:130px;width:44px">Timeline 02<div class="sm">Get out on the water with a great rate</div></div>
  <div class="tl-label" style="left:125px;top:130px;width:44px">Timeline 03<div class="sm">Get out on the water with a great rate</div></div>
  <div class="tl-label" style="left:214px;top:130px;width:46px">Timeline 04<div class="sm">Get out on the water with a great rate</div></div>
  <div class="social" style="top:73px"><span></span><span></span><span></span></div>
  <div class="pagenum">13</div>
</section>

<!-- 14 Portfolio -->
<section class="slide c2 r5">
  <div class="wave"></div>
  <div class="brand" style="font-size:11px;top:17px">TIMREL</div>
  <div class="title caps" style="left:24px;top:15px">Our Portfolio</div>
  <div class="body-text" style="left:24px;top:48px;width:75px;text-align:center">A wonderful serenity has taken possession of my entire soul, like these sweet mornings of spring which I enjoy with my whole heart. I am alone, and feel the charm of existence in this spot, which was created for the bliss of souls like mine.</div>
  <div class="photo" role="img" aria-label="Trimaran sailing at speed" style="left:102px;top:40px;width:85px;height:56px;background:var(--photo-green)"></div>
  <div class="photo" role="img" aria-label="Yachts racing near the coast" style="left:191px;top:40px;width:69px;height:56px;background:var(--photo-blue)"></div>
  <div class="photo" role="img" aria-label="Crew in red jackets on deck" style="left:22px;top:100px;width:165px;height:62px;background:var(--photo-deck)"></div>
  <div class="body-text" style="left:191px;top:102px;width:66px">A wonderful serenity has taken possession of my entire soul, like these sweet mornings of spring which I enjoy with my whole heart.</div>
  <div class="social" style="top:74px"><span></span><span></span><span></span></div>
  <div class="pagenum">14</div>
</section>

<!-- 15 Portfolio -->
<section class="slide c3 r5">
  <div class="wave"></div>
  <div class="brand" style="font-size:11px;top:17px">TIMREL</div>
  <div class="title caps" style="left:24px;top:15px">Our Portfolio</div>
  <div class="photo" role="img" aria-label="Green-hulled racing yacht from above" style="left:26px;top:46px;width:136px;height:90px;background:var(--photo-green)"></div>
  <div class="photo" role="img" aria-label="Yachts racing near the coast" style="left:164px;top:46px;width:59px;height:44px;background:var(--photo-blue)"></div>
  <div class="photo" role="img" aria-label="Catamaran under sail" style="left:164px;top:92px;width:59px;height:44px;background:var(--photo-sea)"></div>
  <div class="body-text" style="left:26px;top:146px;width:178px">A wonderful serenity has taken possession of my entire soul, like these sweet mornings of spring which I enjoy with my whole heart. I am alone, and feel the charm of existence in this spot, which was created for the bliss of souls like mine.</div>
  <div class="social" style="top:74px"><span></span><span></span><span></span></div>
  <div class="pagenum">15</div>
</section>

<!-- 16 Portfolio -->
<section class="slide c1 r6">
  <div class="wave"></div>
  <div class="brand" style="font-size:11px;top:17px">TIMREL</div>
  <div class="title caps" style="left:24px;top:15px">Our Portfolio</div>
  <div class="body-text" style="left:22px;top:47px;width:56px">A wonderful serenity has taken possession of my entire soul, like these sweet mornings of spring which I enjoy with my whole heart. I am alone, and feel the charm of existence in this spot, which was created for the bliss of souls like mine.</div>
  <div class="photo" role="img" aria-label="Yachts racing near the coast" style="left:22px;top:108px;width:56px;height:45px;background:var(--photo-blue)"></div>
  <div class="photo" role="img" aria-label="Green-hulled yacht heeling" style="left:82px;top:67px;width:56px;height:86px;background:var(--photo-green)"></div>
  <div class="photo" role="img" aria-label="Large fleet of sails on grey water" style="left:142px;top:41px;width:56px;height:112px;background:linear-gradient(180deg,#cfd2d4,#8d9396)"></div>
  <div class="body-text" style="left:205px;top:64px;width:56px">A wonderful serenity has taken possession of my entire soul, like these sweet mornings of spring which I enjoy with my whole heart. I am alone, and feel the charm of existence in this spot, which was created for the bliss of souls like mine.</div>
  <div class="social" style="top:74px"><span></span><span></span><span></span></div>
  <div class="pagenum">16</div>
</section>

<!-- 17 Contact -->
<section class="slide c2 r6">
  <div class="wave"></div>
  <div class="brand">TIMREL</div>
  <div class="title" style="left:22px;top:26px">Get Connected With Us</div>
  <div class="photo" role="img" aria-label="Foiling catamarans racing in a harbour" style="left:22px;top:44px;width:171px;height:107px;background:linear-gradient(160deg,#e6e9ec,#9aa7b3 55%,#5a6e82)"></div>
  <div class="abs" style="left:178px;top:53px;width:79px;height:34px;background:var(--teal);border-radius:2px">
    <svg class="abs" style="left:9px;top:9px" width="16" height="16" viewBox="0 0 16 16"><circle cx="8" cy="8" r="8" fill="#fff"/><path d="M5.5 7a2.5 2.5 0 0 1 5 0c0 2-2.5 4.5-2.5 4.5S5.5 9 5.5 7z" fill="#1fa58a"/></svg>
    <div class="abs" style="left:36px;top:10px;font-size:3.6px;color:var(--white)">Description<div style="font-size:2.6px;line-height:1.3;margin-top:2px">Get out on the water<br>with a great rate</div></div>
  </div>
  <div class="abs" style="left:178px;top:92px;width:79px;height:36px;background:var(--teal);border-radius:2px;padding:6px 8px;color:var(--white);font-size:3px;line-height:2.8">
    <div><span style="display:inline-block;width:4px;height:3px;background:#fff;margin-right:5px"></span>youremail@email.com</div>
    <div><span style="display:inline-block;width:4px;height:4px;border-radius:50%;border:.7px solid #fff;margin-right:5px"></span>www.yourwebsite.com</div>
    <div><span style="display:inline-block;width:4px;height:4px;background:#fff;border-radius:1px 2px;margin-right:5px"></span>+1-555-555-5555</div>
  </div>
  <div class="social" style="top:74px"><span></span><span></span><span></span></div>
  <div class="pagenum">17</div>
</section>

<!-- 18 Thank you -->
<section class="slide c3 r6" role="img" aria-label="Yachts and catamarans sailing on deep blue sea" style="background:linear-gradient(180deg,#7f95ae 0%,#1f4f96 12%,#123e84 60%,#0e3270 100%)">
  <div class="brand light">TIMREL</div>
  <div class="abs" style="left:105px;top:104px;font-size:21px;color:var(--white);letter-spacing:.5px">THANK YOU</div>
  <div class="abs" style="left:126px;top:131px;font-size:7px;color:var(--white);letter-spacing:2px">WWW.TIMREL.COM</div>
  <div class="social light" style="left:11px;right:auto;top:107px"><span></span><span></span><span></span></div>
</section>

</body>
</html>
```